Business card and insta posting square

This is for 2 separate projects...

1...a double sided business card for online business (no address) to hand to businesses to get them to list their details on my online directory. the butterfly logo is to be used on the business card.

2.... a posting square for Instagram to write inspirational quotes over the top of to post....with a small butterfly logo somewhere on it (in a corner maybe)....the square is to have a thin, solid green outline around the edge of it, and a faded picture through the background that will allow me to write text over the top of it that will be easily readable.
I would like the same box for all Instagram quote posts for consistency ..

Target Market(s)

spiritual , yoga, meditation, wellness......

Industry/Entity Type

Wellness

Contact Information for Business Card

Details for Business Card...
Wandering The Quiet Tide
Your Complete Wellness Directory
www.wanderingthequiettide.example
insta/FB/pinterest/twitter
*List Your Business for FREE *

Colors
33b8a4
34a7d8
3276b5
876aae
9bcb3c

Requirements
Must have
• butterfly logo included on business card
• insta post square can use the butterfly logo OR the WTQT green square uploaded in the images
Nice to have
• greens

```html
<!DOCTYPE html>
<html lang="en">
<head>
<meta charset="utf-8">
<title>Wandering The Quiet Tide – Business Card</title>
<link href="https://fonts.googleapis.com/css2?family=Bree+Serif&family=Parisienne&family=Lato:wght@400&family=Gochi+Hand&display=swap" rel="stylesheet">
<style>
  :root {
    --backdrop: #2a2c30;
    --card-green: #1f9140;
    --card-edge: #187a34;
    --ink-white: #ffffff;
    --ink-purple: #4b2a7a;
    --mark-violet: #876aae;
    --mark-blue: #34a7d8;
    --rule: rgba(255,255,255,0.45);
  }
  * { margin: 0; padding: 0; box-sizing: border-box; }
  html, body { width: 1200px; height: 900px; overflow: hidden; }
  body {
    background: var(--backdrop);
    display: flex;
    align-items: center;
    justify-content: center;
    gap: 40px;
  }
  .card {
    width: 540px;
    height: 309px;
    background: var(--card-green);
    border-radius: 4px;
    box-shadow: 0 3px 0 var(--card-edge), 0 6px 0 var(--card-edge), 0 14px 24px rgba(0,0,0,0.45);
    position: relative;
    overflow: hidden;
  }
  /* Front */
  .front__headline {
    position: absolute;
    top: 24px;
    left: 30px;
    right: 24px;
    text-align: right;
    white-space: nowrap;
    font-family: "Bree Serif", serif;
    font-size: 30px;
    font-weight: 400;
    color: var(--ink-white);
  }
  .front__mark {
    position: absolute;
    left: 34px;
    top: 88px;
    width: 250px;
    height: 130px;
    border-radius: 6px;
    background: linear-gradient(135deg, var(--mark-violet), var(--mark-blue));
    display: flex;
    align-items: center;
    justify-content: center;
    gap: 12px;
  }
  .front__mark-dot {
    width: 22px; height: 22px; border-radius: 50%;
    background: var(--ink-white);
  }
  .front__mark-name {
    font-family: "Bree Serif", serif;
    font-size: 40px;
    color: var(--ink-white);
  }
  .front__offer {
    position: absolute;
    left: 34px;
    bottom: 26px;
    font-family: "Gochi Hand", cursive;
    font-size: 24px;
    color: var(--ink-purple);
    white-space: nowrap;
  }
  /* Back */
  .back {
    display: flex;
    flex-direction: column;
    align-items: center;
    justify-content: center;
    padding: 0 36px;
    text-align: center;
  }
  .back__name {
    font-family: "Parisienne", cursive;
    font-size: 42px;
    font-weight: 400;
    color: var(--ink-white);
    line-height: 1.2;
    white-space: nowrap;
  }
  .back__url {
    margin-top: 22px;
    font-family: "Lato", sans-serif;
    font-size: 18px;
    color: var(--ink-white);
    white-space: nowrap;
  }
  .back__rule {
    width: 300px;
    height: 1px;
    background: var(--rule);
    margin: 10px 0 12px;
  }
  .back__social { display: flex; gap: 12px; }
  .back__social-slot {
    width: 24px; height: 24px; border-radius: 6px;
    background: var(--ink-white);
  }
</style>
</head>
<body>
  <section class="card front" aria-label="Card front">
    <h1 class="front__headline">Your Complete Wellness Directory</h1>
    <div class="front__mark" role="img" aria-label="Butterfly brand mark area">
      <span class="front__mark-dot"></span>
      <span class="front__mark-name">WTQT</span>
    </div>
    <p class="front__offer">List Your Business for FREE</p>
  </section>

  <section class="card back" aria-label="Card back">
    <h2 class="back__name">Wandering The Quiet Tide</h2>
    <p class="back__url">www.wanderingthequiettide.example</p>
    <div class="back__rule"></div>
    <div class="back__social" aria-label="Social profiles">
      <span class="back__social-slot"></span>
      <span class="back__social-slot"></span>
      <span class="back__social-slot"></span>
      <span class="back__social-slot"></span>
    </div>
  </section>
</body>
</html>
```